Group training gym/bootcamp needs a web design

We need a website for our gym that is based in Sydney. We have indoor functional training classes and outdoor bootcamp classes. We would like the web site to have a video (to be created) and photo gallery. I would like the site made on word press and i would like to be able to make minor changes such as changing images and text without having to use a designer.

The website should have the following pages: home page; the gym; the bootcamp; photo gallery; about us; contact.

I have uploaded our logo and i would like to keep to these colour (blue,yellow,silver) and black is also allowed

Target Market(s)

18-50 male and female

Industry/Entity Type

Gym

Coding

Coded - Design and coding required

Number of Pages Required

5+ page

Font styles to use
Sans Serif

Colors
0692cd
fbed22
1b1b1b
e8e8e8

Requirements
Must have
• The website should have the following pages: home page; the gym; the bootcamp; photo gallery; about us; contact.
• I have uploaded our logo and i would like to keep to these colour (blue,yellow,silver) and black is also allowed
• Video upload and photo upload

```html
<!DOCTYPE html>
<html lang="en">
<head>
<meta charset="utf-8">
<title>Ironline Fitness Hub</title>
<link href="https://fonts.googleapis.com/css2?family=Bebas+Neue&family=Montserrat:wght@400;600;700;800&family=Open+Sans:wght@400;600&display=swap" rel="stylesheet">
<style>
:root{
  --blue:#1f7fd2;
  --blue-dark:#1767b3;
  --yellow:#f0c419;
  --gold:#d4a816;
  --olive:#7c6a12;
  --ink:#1b1b1b;
  --silver:#e8e8e8;
  --grey:#8a8a8a;
  --white:#ffffff;
}
*{box-sizing:border-box;margin:0;padding:0}
html,body{width:1200px;height:3774px;overflow:hidden;background:var(--white)}
body{font-family:"Open Sans",Arial,sans-serif;color:var(--ink)}
.page{position:relative;width:1200px;height:3774px;overflow:hidden}
.abs{position:absolute}
.photo{position:absolute;overflow:hidden}
.heading{font-family:"Bebas Neue",Impact,sans-serif;letter-spacing:1px;line-height:1}
.btn{position:absolute;display:flex;align-items:center;justify-content:center;border-radius:24px;font-family:"Montserrat",Arial,sans-serif;font-size:17px;font-weight:600;letter-spacing:.5px;color:var(--white);background:var(--blue);box-shadow:0 4px 0 rgba(0,0,0,.15)}
.para{font-size:13.5px;line-height:1.6}

/* header */
.header{position:absolute;left:0;top:0;width:1200px;height:126px;background:#f2f2f2}
.header-bar{position:absolute;left:0;top:0}
.brand{position:absolute;left:70px;top:32px;display:flex;align-items:center;gap:12px}
.brand-mark{width:30px;height:30px;background:var(--blue)}
.brand-name{font-family:"Montserrat",Arial,sans-serif;font-weight:800;font-size:22px;color:var(--blue);letter-spacing:.5px;line-height:1.05;text-transform:uppercase}
.top-contact{position:absolute;left:748px;top:24px;display:flex;align-items:center;gap:8px;color:var(--white);font-family:"Montserrat",sans-serif;font-size:16px;font-weight:600}
.search{position:absolute;left:892px;top:22px;width:232px;height:30px;border-radius:15px;background:var(--white);font-size:12px;color:#aaa;padding:7px 16px}
.search-btn{position:absolute;right:2px;top:2px;width:26px;height:26px;border-radius:50%;background:var(--yellow);display:flex;align-items:center;justify-content:center}
.nav{position:absolute;left:534px;top:78px;display:flex;gap:0;font-family:"Montserrat",sans-serif;font-size:15px;font-weight:600;color:var(--white)}
.nav a{color:var(--white);text-decoration:none;padding:0 13px 8px}
.nav a.active{border-bottom:2px solid var(--white)}

/* hero */
.hero{position:absolute;left:0;top:126px;width:1200px;height:533px;overflow:hidden}
.hero-title{position:absolute;left:80px;top:64px;color:var(--white);font-family:"Montserrat",sans-serif;font-weight:800;font-size:44px;line-height:1.1;text-transform:uppercase}
.hero-btn{left:78px;top:164px;width:178px;height:46px;background:var(--white);color:var(--ink);font-weight:700}
.arrows{position:absolute;display:flex;gap:8px}
.arrows span{width:30px;height:30px;display:flex;align-items:center;justify-content:center;border:2px solid var(--white);color:var(--white);font-size:18px;font-weight:700;line-height:1}
.arrows span.dim{background:rgba(0,0,0,.4)}
.dots{position:absolute;right:30px;bottom:15px;display:flex;gap:8px}
.dots span{width:14px;height:14px;background:var(--white);border:2px solid #555}
.dots span.on{background:#333}

/* welcome */
.welcome-title{position:absolute;left:0;top:704px;width:1200px;text-align:center;font-size:46px}
.welcome-text{position:absolute;left:175px;top:766px;width:850px;text-align:center;color:#444}
.blue{color:var(--blue)}
.gold{color:var(--gold)}

/* gallery */
.gallery-band{position:absolute;left:0;top:951px;width:1200px;height:307px;background:linear-gradient(180deg,#f5cc1f,#eebf12)}
.gallery-title{position:absolute;left:280px;top:996px;width:260px;text-align:center;font-size:44px;color:var(--ink)}
.gallery-text{position:absolute;left:110px;top:1060px;width:590px;text-align:center;color:#333}
.gallery-box{position:absolute;left:106px;top:1152px;width:988px;height:282px;border-radius:18px;background:linear-gradient(180deg,#ffffff 0%,#ffffff 60%,#d9ecfa 100%)}

/* indoor */
.indoor{position:absolute;left:0;top:1555px;width:1200px;height:513px;background:linear-gradient(120deg,#2c2c2c,#1b1b1b 55%,#303030)}
.indoor-title{position:absolute;left:106px;top:100px;font-size:46px}
.indoor-text{position:absolute;left:106px;top:172px;width:600px;color:#ddd}

/* trainers */
.section-title{position:absolute;left:0;width:1200px;text-align:center;font-size:46px}
.trainer-card{position:absolute;top:2181px;width:254px;height:310px;border:1px solid #d8d8d8;background:var(--white)}
.trainer-card .photo{left:8px;top:8px;width:236px;height:292px}
.trainer-name{position:absolute;top:2508px;font-family:"Bebas Neue",sans-serif;font-size:24px;letter-spacing:1px}
.trainer-role{position:absolute;top:2540px;font-family:"Montserrat",sans-serif;font-size:12px;color:#aaa;text-transform:uppercase}

/* testimonial */
.quote-box{position:absolute;left:166px;top:3039px;width:590px;height:214px;border:2px solid #e3cc6e;background:var(--white)}
.quote-text{position:absolute;left:58px;top:40px;width:480px;text-align:center;color:#555}
.quote-name{position:absolute;left:222px;top:130px;font-family:"Bebas Neue",sans-serif;font-size:22px;letter-spacing:1px}
.quote-role{position:absolute;left:260px;top:154px;font-size:11px;color:#aaa}
.thumb{position:absolute;top:3102px;width:74px;height:74px;border:3px solid var(--white);box-shadow:0 0 0 1px #ccc}

/* footer */
.footer{position:absolute;left:0;top:3303px;width:1200px;height:471px;overflow:hidden;background:#141414}
.foot-head{position:absolute;top:58px;font-size:28px;color:var(--white)}
.foot-links{position:absolute;left:78px;top:108px;list-style:none;font-family:"Montserrat",sans-serif;font-size:13px;text-transform:uppercase}
.foot-links li{height:36px;color:var(--gold)}
.foot-links li.active{color:var(--white)}
.field{position:absolute;height:42px;border:1px solid var(--gold);color:#ddd;font-size:13px;padding:11px 14px}
.contact-line{position:absolute;left:810px;display:flex;gap:12px;color:var(--white);font-size:13px;line-height:1.6}
.foot-brand{position:absolute;left:930px;top:408px;display:flex;align-items:center;gap:8px}
.foot-brand .brand-mark{width:14px;height:14px;background:var(--gold)}
.foot-brand .brand-name{font-size:14px;color:var(--white)}
.rights{position:absolute;left:952px;top:432px;font-size:12px;color:var(--white)}
</style>
</head>
<body>
<div class="page">

  <!-- header -->
  <header class="header">
    <svg class="header-bar" width="1200" height="126" viewBox="0 0 1200 126">
      <polygon points="500,0 1200,0 1200,126 430,126" fill="#1f7fd2"/>
      <polygon points="440,0 500,0 430,126 370,126" fill="#cfe6f7" opacity=".6"/>
    </svg>
    <div class="brand">
      <div class="brand-mark"></div>
      <div class="brand-name">Ironline<br>Fitness Hub</div>
    </div>
    <div class="top-contact">
      <svg width="18" height="18" viewBox="0 0 24 24"><path d="M6.6 10.8a15 15 0 0 0 6.6 6.6l2.2-2.2c.3-.3.7-.4 1-.2 1.1.4 2.3.6 3.6.6.6 0 1 .4 1 1V20c0 .6-.4 1-1 1A17 17 0 0 1 3 4c0-.6.4-1 1-1h3.5c.6 0 1 .4 1 1 0 1.3.2 2.5.6 3.6.1.3 0 .7-.2 1z" fill="#fff"/></svg>
      123 555 0190
    </div>
    <div class="search">Search...
      <div class="search-btn"><svg width="13" height="13" viewBox="0 0 24 24"><circle cx="10" cy="10" r="7" fill="none" stroke="#1b1b1b" stroke-width="3"/><line x1="15" y1="15" x2="22" y2="22" stroke="#1b1b1b" stroke-width="3"/></svg></div>
    </div>
    <nav class="nav">
      <a class="active">HOME</a><a>THE GYM</a><a>THE BOOTCAMP</a><a>GALLERY</a><a>ABOUT US</a><a>CONTACT</a>
    </nav>
  </header>

  <!-- hero -->
  <section class="hero">
    <div class="photo" role="img" aria-label="Athlete with toned body lifting a dumbbell" style="left:0;top:0;width:1200px;height:533px;background:linear-gradient(100deg,#3a3a3a 0%,#6e5a48 40%,#a58068 55%,#3c3c3c 75%,#222 100%)"></div>
    <svg class="abs" style="left:0;top:0" width="1200" height="533" viewBox="0 0 1200 533">
      <polygon points="0,0 420,0 90,533 0,533" fill="#7c6a12" opacity=".85"/>
      <polygon points="0,250 200,533 0,533" fill="#5b4d0c" opacity=".9"/>
      <polygon points="860,0 1200,0 1200,533 1060,533" fill="#6d5c10" opacity=".85"/>
      <polygon points="780,0 900,0 760,533 660,533" fill="#c9a21a" opacity=".35"/>
    </svg>
    <h1 class="hero-title">Achieve your<br>fitness goals!</h1>
    <div class="btn hero-btn">START TODAY</div>
    <div class="arrows" style="left:78px;top:246px"><span class="dim">«</span><span>»</span></div>
    <div class="dots"><span></span><span class="on"></span><span></span></div>
  </section>

  <!-- welcome -->
  <h2 class="heading welcome-title"><span class="blue">Welcome to</span> <span class="gold">Ironline Fitness Hub</span></h2>
  <p class="para welcome-text">Lorem Ipsum is simply dummy text of the printing and typesetting industry. Lorem Ipsum has been the industry's standard dummy text ever since the 1500s, when an unknown printer took a galley of type and scrambled it to make a type specimen book. It has survived not only five centuries.</p>
  <div class="btn" style="left:526px;top:855px;width:180px;height:44px">READ MORE</div>

  <!-- gallery -->
  <div class="gallery-band"></div>
  <h2 class="heading gallery-title">Gallery</h2>
  <p class="para gallery-text">Lorem Ipsum is simply dummy text of the printing and typesetting industry. Lorem Ipsum has been.</p>
  <div class="photo" role="img" aria-label="Stacked gallery photos of women training in the gym" style="left:745px;top:946px;width:310px;height:236px;background:linear-gradient(135deg,#9b8a7c,#c8b4a4 50%,#6c5a5a);transform:rotate(6deg);border:6px solid #fff;box-shadow:0 4px 10px rgba(0,0,0,.35)"></div>
  <div class="gallery-box"></div>
  <div class="photo" role="img" aria-label="Trainer coaching a client with a barbell outdoors" style="left:126px;top:1208px;width:294px;height:206px;background:linear-gradient(180deg,#8cc3ea,#cfe4f2 55%,#7a4b3a)"></div>
  <div class="photo" role="img" aria-label="Woman using a weight machine in the gym" style="left:453px;top:1208px;width:292px;height:206px;background:linear-gradient(160deg,#d8d8d8,#9a9a9a 60%,#6a6a6a)"></div>
  <div class="photo" role="img" aria-label="Group of women smiling on exercise mats" style="left:782px;top:1208px;width:292px;height:206px;background:linear-gradient(180deg,#b9d6e8,#e0b5a0 55%,#6d8fb8)"></div>
  <div class="btn" style="left:508px;top:1457px;width:180px;height:46px">VIEW ALL</div>

  <!-- indoor -->
  <section class="indoor">
    <div class="photo" role="img" aria-label="Dim gym interior with equipment" style="left:0;top:0;width:1200px;height:513px;background:linear-gradient(90deg,rgba(60,60,60,.35),rgba(20,20,20,.2))"></div>
    <h2 class="heading indoor-title"><span class="blue">Indoor functional</span> <span class="gold">training classes</span></h2>
    <p class="para indoor-text">Lorem Ipsum is simply dummy text of the printing and typesetting industry. Lorem Ipsum has been the industry's standard dummy text ever since the 1500s, when an unknown printer took a galley of type and scrambled it to make a type specimen book. It has survived not only five centuries.Lorem Ipsum is simply dummy text of the printing and typesetting industry. Lorem Ipsum has been the industry's standard dummy text ever since the 1500s, when an unknown printer took a galley of type and scrambled it to make a type specimen book. It has survived not only five centuries.</p>
    <div class="btn" style="left:106px;top:337px;width:176px;height:46px">READ MORE</div>
    <svg class="abs" style="left:860px;top:50px" width="240" height="380" viewBox="0 0 240 380"><polygon points="60,0 240,0 200,380 20,380" fill="#f0c419"/></svg>
    <div class="photo" role="img" aria-label="Muscular man curling a dumbbell" style="left:755px;top:55px;width:330px;height:370px;background:radial-gradient(ellipse at 55% 45%,#c99a78,#8a6248 55%,rgba(40,40,40,0) 75%)"></div>
    <div class="arrows" style="left:923px;top:433px"><span class="dim">«</span><span>»</span></div>
  </section>

  <!-- trainers -->
  <h2 class="heading section-title" style="top:2112px"><span class="blue">Our</span> <span class="gold">Trainer</span></h2>
  <div class="trainer-card" style="left:78px"><div class="photo" role="img" aria-label="Female trainer in sports top" style="background:linear-gradient(180deg,#fff,#f1d7cc 40%,#e07aa0 70%,#fff)"></div></div>
  <div class="trainer-card" style="left:342px"><div class="photo" role="img" aria-label="Male bodybuilder holding dumbbells" style="background:linear-gradient(180deg,#fff,#d9ac86 45%,#4a4a4a 80%,#fff)"></div></div>
  <div class="trainer-card" style="left:604px">
    <div class="photo" role="img" aria-label="Female trainer with social links overlay" style="background:linear-gradient(180deg,#fff,#f5e2d8 40%,#f0a9c4 60%,#d8d8d8 85%,#fff);opacity:.55"></div>
    <svg class="abs" style="left:60px;top:60px" width="134" height="190" viewBox="0 0 134 190">
      <line x1="10" y1="30" x2="124" y2="160" stroke="#1b1b1b" stroke-width="2"/>
      <line x1="124" y1="30" x2="10" y2="160" stroke="#1b1b1b" stroke-width="2"/>
      <circle cx="67" cy="44" r="10" fill="#1b1b1b"/><circle cx="22" cy="95" r="10" fill="#1b1b1b"/>
      <circle cx="112" cy="95" r="10" fill="#1b1b1b"/><circle cx="67" cy="146" r="10" fill="#1b1b1b"/>
    </svg>
  </div>
  <div class="trainer-card" style="left:868px"><div class="photo" role="img" aria-label="Male trainer in black tank top" style="background:linear-gradient(180deg,#fff,#c7966f 35%,#1e1e1e 60%,#fff)"></div></div>
  <div class="trainer-name" style="left:88px">- Dana Harlow</div><div class="trainer-role" style="left:90px">Body builder</div>
  <div class="trainer-name" style="left:352px">- Dana Harlow</div><div class="trainer-role" style="left:354px">Body builder</div>
  <div class="trainer-name" style="left:614px">- Dana Harlow</div><div class="trainer-role" style="left:616px">Body builder</div>
  <div class="trainer-name" style="left:878px">- Dana Harlow</div><div class="trainer-role" style="left:880px">Body builder</div>

  <!-- photo strip -->
  <div class="photo" role="img" aria-label="Two women doing lunges with a balance ball" style="left:0;top:2612px;width:390px;height:312px;background:linear-gradient(135deg,#eef1f3,#c9d2d8 55%,#7a8ea3)"></div>
  <div class="photo" role="img" aria-label="Video still of a woman lifting a barbell in a dark gym" style="left:400px;top:2612px;width:400px;height:312px;background:radial-gradient(ellipse at 45% 40%,#7b5a44,#2a2522 65%,#141414)"></div>
  <svg class="abs" style="left:568px;top:2736px" width="64" height="64" viewBox="0 0 64 64"><circle cx="32" cy="32" r="29" fill="rgba(0,0,0,.55)" stroke="#fff" stroke-width="3"/><polygon points="25,19 46,32 25,45" fill="#fff"/></svg>
  <div class="photo" role="img" aria-label="Trainer spotting a man curling dumbbells" style="left:810px;top:2612px;width:390px;height:312px;background:linear-gradient(135deg,#f2f2f2,#b9c4cc 45%,#4d5560)"></div>

  <!-- testimonial -->
  <h2 class="heading section-title blue" style="top:2972px">Testimonial</h2>
  <div class="quote-box">
    <p class="para quote-text">"Lorem Ipsum is simply dummy text of the printing and typesetting industry. Lorem Ipsum has been the industry's standard dummy text ever since the 1500s, when an unknown printer took a galley of type and scrambled it to make a type specimen book. It has survived not only five centuries."</p>
    <svg class="abs" style="left:218px;top:174px" width="20" height="16" viewBox="0 0 20 16"><path d="M0 16V9C0 4 3 1 8 0v3C5 4 4 6 4 8h4v8zM11 16V9c0-5 3-8 8-9v3c-3 1-4 3-4 5h4v8z" fill="#1f7fd2"/></svg>
    <div class="quote-name" style="left:248px;top:168px">- Dana Harlow</div>
    <div class="quote-role" style="left:258px;top:192px">designation</div>
  </div>
  <div class="thumb" role="img" aria-label="Client portrait" style="left:715px;background:linear-gradient(180deg,#dde8f0,#2e4d7a)"></div>
  <div class="thumb" role="img" aria-label="Client portrait" style="left:798px;background:linear-gradient(180deg,#f1ece6,#b07a5e)"></div>
  <div class="thumb" role="img" aria-label="Client portrait" style="left:881px;background:linear-gradient(180deg,#7da8d4,#d85a6a)"></div>
  <div class="thumb" role="img" aria-label="Client portrait" style="left:963px;background:linear-gradient(180deg,#eee,#3a3a3a)"></div>

  <!-- footer -->
  <footer class="footer">
    <div class="photo" role="img" aria-label="Faint silhouette of an athlete" style="left:380px;top:0;width:420px;height:471px;background:radial-gradient(ellipse at 50% 45%,#3a3a3a,rgba(20,20,20,0) 70%)"></div>
    <svg class="abs" style="left:0;top:0" width="1200" height="471" viewBox="0 0 1200 471">
      <polygon points="0,0 330,0 0,300" fill="#6d5c10" opacity=".9"/>
      <polygon points="1200,90 1200,471 820,471" fill="#7c6a12"/>
    </svg>
    <h3 class="heading foot-head" style="left:78px">Quick links</h3>
    <ul class="foot-links">
      <li class="active">Home</li><li>The gym</li><li>The bootcamp</li><li>Gallery</li><li>About us</li><li>Contact</li>
    </ul>

    <h3 class="heading foot-head" style="left:350px">Get in touch</h3>
    <p class="abs para" style="left:350px;top:98px;width:360px;color:#fff;font-size:13px">"Lorem Ipsum is simply dummy text of the printing and typesetting industry.</p>
    <div class="field" style="left:350px;top:156px;width:178px">Name</div>
    <div class="field" style="left:536px;top:156px;width:181px">Contact No.</div>
    <div class="field" style="left:350px;top:212px;width:367px">E-mail ID</div>
    <div class="field" style="left:350px;top:252px;width:367px;height:76px">Message...</div>
    <div class="btn" style="left:443px;top:335px;width:176px;height:46px;background:var(--yellow);color:var(--ink)">READ MORE</div>

    <h3 class="heading foot-head" style="left:810px">Contact us</h3>
    <div class="contact-line" style="top:102px">
      <svg width="14" height="20" viewBox="0 0 14 20"><path d="M7 0a7 7 0 0 0-7 7c0 5 7 13 7 13s7-8 7-13a7 7 0 0 0-7-7zm0 10a3 3 0 1 1 0-6 3 3 0 0 1 0 6z" fill="#d4a816"/></svg>
      <div>IRONLINE FITNESS HUB<br>Lorem ipsum dummy text,<br>Country,123456.</div>
    </div>
    <div class="contact-line" style="top:192px">
      <svg width="14" height="16" viewBox="0 0 24 24"><path d="M6.6 10.8a15 15 0 0 0 6.6 6.6l2.2-2.2c.3-.3.7-.4 1-.2 1.1.4 2.3.6 3.6.6.6 0 1 .4 1 1V20c0 .6-.4 1-1 1A17 17 0 0 1 3 4c0-.6.4-1 1-1h3.5c.6 0 1 .4 1 1 0 1.3.2 2.5.6 3.6.1.3 0 .7-.2 1z" fill="#d4a816"/></svg>
      <div>123 555 0190</div>
    </div>
    <div class="contact-line" style="top:232px">
      <svg width="16" height="14" viewBox="0 0 16 12"><rect width="16" height="12" fill="#d4a816"/><polyline points="0,0 8,7 16,0" fill="none" stroke="#141414" stroke-width="1.5"/></svg>
      <div>hello@ironlinefitness.com</div>
    </div>
    <div class="foot-brand"><div class="brand-mark"></div><div class="brand-name">IRONLINE FITNESS HUB</div></div>
    <div class="rights">All Rights Reserved.</div>
  </footer>

</div>
</body>
</html>
```